Business card design for a engineering company

I need a double sided business card design for my company "Verdmont Flow Solutions". The card will be used in Malaysia. Sleek and professional, with a little design flare to it.
Information to showcase:
1. Company logo
2. Name, title, phone, email address, website address
3. our products "Pumping technology, Valve & actuation, Air Moving Technology
Example:
Ravi Tanaka
Business manager
ravi.tanaka@verdmont-example.com
www.verdmont-example.com.my
- Pumping technology
- Valve & actuation
- Air moving technology
Target Market(s)
engineers, purchasing managers
Industry/Entity Type
Business
Contact Information for Business Card
Ravi Tanaka
Business manager
ravi.tanaka@verdmont-example.com
www.verdmont-example.com.my
- Pumping technology
- Valve & actuation
- Air moving technology
catch phrase : "Solving flow challenges, exceeding expectations"

```html
<!DOCTYPE html>
<html lang="en">
<head>
<meta charset="utf-8">
<title>Verdmont Flow Solutions – Business Card</title>
<link rel="stylesheet" href="https://fonts.googleapis.com/css2?family=Questrial&display=swap">
<style>
  :root {
    --navy: #12303e;
    --navy-light: #2d4f60;
    --navy-dark: #0f2733;
    --orange: #f39321;
    --orange-deep: #ee6a34;
    --grey-bg: #a3a3a3;
    --white: #ffffff;
    --text-light: #e8eef1;
  }
  * { box-sizing: border-box; margin: 0; padding: 0; }
  html, body {
    width: 1200px; height: 900px; overflow: hidden;
    background: var(--grey-bg);
    font-family: "Questrial", "Century Gothic", sans-serif;
  }
  .sheet {
    width: 1200px; height: 900px;
    display: flex; flex-direction: column;
    align-items: center; justify-content: center; gap: 40px;
  }
  .card {
    width: 700px; height: 400px;
    position: relative; overflow: hidden;
    box-shadow: 0 6px 18px rgba(0,0,0,0.25);
  }

  /* Front */
  .card--front { background: var(--white); }
  .brand {
    position: absolute; left: 150px; top: 110px;
    display: flex; align-items: center; gap: 22px;
  }
  .brand__dot {
    width: 70px; height: 70px; border-radius: 50%;
    background: var(--orange);
  }
  .brand__name {
    color: var(--navy);
    font-size: 50px; line-height: 1;
    letter-spacing: 1px;
  }
  .brand__name span {
    display: block; font-size: 19px; letter-spacing: 10px; margin-top: 8px;
  }
  .tagline-band {
    position: absolute; left: 0; right: 0; bottom: 46px; height: 46px;
    background: var(--navy);
    display: flex; align-items: center; padding-left: 70px;
    color: var(--white); font-size: 21px; letter-spacing: 0.3px;
  }
  .tagline-band__accent {
    position: absolute; right: 0; top: -46px;
    width: 46px; height: 46px; background: var(--orange);
  }

  /* Back */
  .card--back {
    background: linear-gradient(135deg, var(--navy-light) 0%, var(--navy) 60%, var(--navy-dark) 100%);
    color: var(--text-light);
  }
  .back-brand {
    position: absolute; left: 70px; top: 150px;
    display: flex; align-items: center; gap: 18px;
  }
  .back-brand__dot {
    width: 90px; height: 90px; border-radius: 50%;
    background: linear-gradient(135deg, var(--orange), var(--orange-deep));
  }
  .back-brand__name {
    color: var(--text-light); font-size: 18px; line-height: 1.3; letter-spacing: 2px;
  }
  .contact {
    position: absolute; left: 360px; top: 60px;
  }
  .contact__name { font-size: 36px; font-weight: 700; color: var(--white); line-height: 1.1; }
  .contact__name .surname { color: var(--orange); }
  .contact__title { font-size: 22px; margin-bottom: 26px; }
  .contact__line { font-size: 15px; line-height: 1.5; }
  .contact__web { color: var(--orange); }
  .products {
    position: absolute; left: 70px; right: 40px; bottom: 34px;
    font-size: 18px; color: var(--text-light);
  }
  .products .highlight { color: var(--orange); }
</style>
</head>
<body>
<main class="sheet">
  <section class="card card--front" aria-label="Card front">
    <div class="brand">
      <div class="brand__dot"></div>
      <div class="brand__name">VERDMONT<span>FLOW SOLUTIONS</span></div>
    </div>
    <div class="tagline-band">
      Solving flow challenges, exceeding expectations
      <div class="tagline-band__accent"></div>
    </div>
  </section>

  <section class="card card--back" aria-label="Card back">
    <div class="back-brand">
      <div class="back-brand__dot"></div>
      <div class="back-brand__name">VERDMONT<br>FLOW SOLUTIONS</div>
    </div>
    <div class="contact">
      <p class="contact__name">Ravi <span class="surname">Tanaka</span></p>
      <p class="contact__title">Business manager</p>
      <p class="contact__line">555 014 2270</p>
      <p class="contact__line">ravi.tanaka@verdmont-example.com</p>
      <p class="contact__line contact__web">www.verdmont-example.com.my</p>
    </div>
    <p class="products">Pumping technology - <span class="highlight">Valve &amp; actuation</span> - Air moving technology</p>
  </section>
</main>
</body>
</html>
```